Stationery and Business Card Design

We need stationary design for our new company pelvanta. Pelvanta is a company that provides city apartment rentals for tourists in Athens We need business cards, letterheads for A4 and A5 and envelopes for A4 A5. The design needs to be modern, friendly and corporate.

Target Market(s)

City Tourists

Industry/Entity Type

Tourism

```html
<!DOCTYPE html>
<html lang="en">
<head>
<meta charset="utf-8">
<title>Pelvanta Business Card</title>
<link href="https://fonts.googleapis.com/css2?family=Raleway:wght@400;500;600&display=swap" rel="stylesheet">
<style>
  :root {
    --backdrop: #a9a6a7;
    --brand: #832056;
    --brand-dark: #4a2a3a;
    --paper: #f4f4f4;
    --ink: #3a3a3a;
    --white: #ffffff;
  }
  html, body {
    margin: 0;
    padding: 0;
    width: 1200px;
    height: 1200px;
    overflow: hidden;
    background: var(--backdrop);
    font-family: 'Raleway', sans-serif;
  }
  .canvas {
    position: relative;
    width: 1200px;
    height: 1200px;
  }
  .card {
    position: absolute;
    border-radius: 22px;
    overflow: hidden;
  }
  .card-front {
    left: 238px;
    top: 118px;
    width: 713px;
    height: 419px;
    background: var(--brand);
  }
  .front-mark {
    position: absolute;
    left: 303px;
    top: 113px;
    width: 100px;
    height: 100px;
    background: var(--white);
  }
  .front-name {
    position: absolute;
    left: 0;
    right: 0;
    top: 218px;
    text-align: center;
    color: var(--white);
    font-size: 62px;
    font-weight: 500;
    letter-spacing: -0.5px;
  }
  .card-back {
    left: 231px;
    top: 644px;
    width: 711px;
    height: 417px;
    background: var(--paper);
  }
  .back-band {
    position: absolute;
    left: 0;
    top: 0;
    bottom: 0;
    width: 60px;
    background: var(--brand);
    border-right: 7px solid var(--brand-dark);
  }
  .back-logo {
    position: absolute;
    left: 343px;
    top: 51px;
    display: flex;
    align-items: center;
    gap: 24px;
  }
  .back-mark {
    width: 74px;
    height: 72px;
    background: var(--brand);
  }
  .back-name {
    color: var(--brand);
    font-size: 42px;
    font-weight: 500;
  }
  .person {
    position: absolute;
    left: 96px;
    top: 192px;
  }
  .person-name {
    color: var(--brand);
    font-size: 26px;
    font-weight: 600;
    margin: 0;
  }
  .person-title {
    color: var(--ink);
    font-size: 18px;
    margin: 4px 0 0;
  }
  .contacts {
    position: absolute;
    left: 96px;
    top: 283px;
    margin: 0;
    padding: 0;
    list-style: none;
    color: var(--ink);
    font-size: 18px;
  }
  .contacts li {
    display: flex;
    align-items: center;
    height: 24px;
  }
  .contacts svg {
    width: 16px;
    height: 16px;
    margin-right: 17px;
    fill: var(--brand);
  }
  .accent { color: var(--brand); }
  .address {
    position: absolute;
    left: 96px;
    top: 362px;
    margin: 0;
    color: var(--ink);
    font-size: 18px;
  }
</style>
</head>
<body>
<main class="canvas">
  <section class="card card-front" aria-label="Card front">
    <div class="front-mark"></div>
    <div class="front-name">Pelvanta</div>
  </section>

  <section class="card card-back" aria-label="Card back">
    <div class="back-band"></div>
    <div class="back-logo">
      <div class="back-mark"></div>
      <div class="back-name">Pelvanta</div>
    </div>
    <div class="person">
      <p class="person-name">Daria Kostel</p>
      <p class="person-title">Your Title</p>
    </div>
    <ul class="contacts">
      <li>
        <svg viewBox="0 0 16 16" aria-hidden="true"><path d="M2 5c0-2 2-3 6-3s6 1 6 3v1h-3V5H5v1H2zM4 7h8l2 7H2z"/><circle cx="8" cy="10" r="1.8" fill="#f4f4f4"/></svg>
        +00 111 222 3333
      </li>
      <li>
        <svg viewBox="0 0 16 16" aria-hidden="true"><path d="M8 1a7 7 0 1 0 0 14A7 7 0 0 0 8 1zm0 1.5c.8 0 1.7 1.4 2 3.8H6c.3-2.4 1.2-3.8 2-3.8zM2.6 7.3h2.3v1.4H2.6zm3.3 0h4.2v1.4H5.9zm5.2 0h2.3v1.4h-2.3zM6 9.7h4c-.3 2.4-1.2 3.8-2 3.8s-1.7-1.4-2-3.8z"/></svg>
        <span>www.<span class="accent">yourwebsite</span>.com</span>
      </li>
      <li>
        <svg viewBox="0 0 16 16" aria-hidden="true"><path d="M1 3h14v10H1zm1.5 1.3v.4L8 9l5.5-4.3v-.4zm0 2.2v5.2h11V6.5L8 10.8z"/></svg>
        yourname@yourwebsite.com
      </li>
    </ul>
    <p class="address">Your Long Commercial or business address in 2 line</p>
  </section>
</main>
</body>
</html>
```